2 Creative Website Banners for Furniture Brand

Morning Tobrasca....
The get a great night sleep banner is complete - we are happy with that one.
Ive uploaded a slightly different concept for the other banner below. This is just something rough ive thrown together. But you can see I have added a curve, a maroon coloured background which is slightly transparent and a big heart in the background....
I do not necessarily want to use this heart image but something a bit like this (a nice graphic, gif etc) but something quite elegant faded in, or perhaps a number of hearts (done in a tasteful way). Also can we keep the typography in the same format as you can see for this one.
Nearly there :)!
Industry/Entity Type
Furniture

```html
<!DOCTYPE html>
<html lang="en">
<head>
<meta charset="utf-8">
<title>Furniture Banners – Find A Look You Love</title>
<link href="https://fonts.googleapis.com/css2?family=Josefin+Sans:wght@300;400&family=Playfair+Display:wght@400&family=Quicksand:wght@400;500&display=swap" rel="stylesheet">
<style>
  :root{
    --page:#e3e6ee;
    --plum-deep:#2b0f2c;
    --plum:#4a1f45;
    --gold:#f0c27a;
    --tan-light:#ecd3a4;
    --tan:#c9a16b;
    --ink-plum:#3a1737;
    --white:#ffffff;
    --taupe:#5b4e53;
    --photo-a:#3a3034;
    --photo-b:#7d6a72;
    --photo-c:#4c5059;
  }
  *{box-sizing:border-box;margin:0;padding:0}
  html,body{width:1200px;height:1200px;overflow:hidden;background:var(--page)}
  .canvas{position:relative;width:1200px;height:1200px}

  .banner{
    --s:1;
    position:absolute;
    width:calc(1103px*var(--s));height:calc(327px*var(--s));
    display:flex;overflow:hidden;
  }
  .banner--shadow{box-shadow:0 8px 14px rgba(0,0,0,.35)}
  .banner__panel{
    position:relative;width:calc(561px*var(--s));height:100%;flex:none;overflow:hidden;
  }
  .banner--plum .banner__panel{background:linear-gradient(160deg,#5a2a52 0%,var(--plum) 35%,var(--plum-deep) 100%)}
  .banner--tan .banner__panel{background:linear-gradient(160deg,var(--tan) 0%,#d9b47c 45%,var(--tan-light) 100%)}
  .banner__decor{position:absolute;inset:0;width:100%;height:100%}
  .banner--plum .banner__decor{color:var(--gold)}
  .banner--tan .banner__decor{color:var(--white)}
  .banner__hearts{opacity:.09}
  .banner__curve{opacity:.35}
  .banner__photo{
    flex:1;height:100%;
    background:
      radial-gradient(ellipse at 30% 75%,var(--photo-b) 0%,transparent 55%),
      linear-gradient(90deg,var(--photo-a) 0%,#5d4c55 45%,var(--photo-c) 75%,#2a2b30 100%);
  }
  .banner__kicker,.banner__title{
    position:absolute;left:0;width:100%;text-align:center;
  }
  .banner__kicker{
    top:calc(38px*var(--s));
    font:300 calc(40px*var(--s))/1 "Josefin Sans",sans-serif;
    letter-spacing:calc(0.5px*var(--s));
    padding-right:calc(12px*var(--s));
  }
  .banner__title{
    top:calc(80px*var(--s));
    font:400 calc(128px*var(--s))/1 "Playfair Display",serif;
    letter-spacing:calc(8px*var(--s));
    padding-right:calc(10px*var(--s));
  }
  .banner__tagline{
    position:absolute;left:calc(51px*var(--s));top:calc(212px*var(--s));
    width:calc(458px*var(--s));height:calc(71px*var(--s));
    border:calc(1.2px*var(--s)) solid;
    display:flex;align-items:center;justify-content:center;text-align:center;
    font:400 calc(20.5px*var(--s))/1.2 "Quicksand",sans-serif;
  }
  .banner--plum .banner__kicker,.banner--plum .banner__title{color:var(--gold)}
  .banner--plum .banner__tagline{color:var(--white);border-color:var(--gold)}
  .banner--tan .banner__kicker,.banner--tan .banner__title{color:var(--white)}
  .banner--tan .banner__tagline{color:var(--ink-plum);border-color:var(--ink-plum)}

  .banner--top{left:49px;top:34px}
  .banner--bottom{left:49px;top:396px}

  /* website homepage */
  .site{
    position:absolute;left:335px;top:796px;width:530px;height:299px;
    background:var(--white);overflow:hidden;box-shadow:0 6px 16px rgba(0,0,0,.25);
  }
  .site__notice{height:7px;background:#f4f1f1;font:400 3.5px/7px "Quicksand",sans-serif;text-align:center;color:#7a6a70}
  .site__header{position:relative;height:39px}
  .site__brand{position:absolute;left:16px;top:13px;font:400 11px/1 "Josefin Sans",sans-serif;letter-spacing:1.5px;color:var(--ink-plum)}
  .site__brand small{display:block;font-size:3px;letter-spacing:.6px;text-align:center;color:var(--tan);margin-top:2px}
  .site__brand::after{content:"";display:block;width:64px;height:1.5px;background:var(--ink-plum);margin-top:2px}
  .site__phone{position:absolute;right:22px;top:11px;font:400 8px/1 "Josefin Sans",sans-serif;color:var(--ink-plum);display:flex;align-items:center;gap:3px}
  .site__phone i{width:6px;height:6px;border-radius:50%;background:#b0243b;display:block}
  .site__links{position:absolute;right:22px;top:27px;display:flex;gap:10px;font:400 3px/1 "Quicksand",sans-serif;color:#555}
  .site__links span::before{content:"";display:inline-block;width:3px;height:4px;border:.5px solid var(--tan);margin-right:2px;vertical-align:middle}
  .site__nav{height:14px;background:var(--taupe);display:flex;justify-content:center;gap:26px;font:400 3.6px/14px "Quicksand",sans-serif;color:var(--white)}
  .site__hero{position:absolute;left:0;top:60px;width:530px !important;height:134px !important;box-shadow:none}
  .site__hero .banner__panel{width:268px}
  .site__hero .banner__kicker,.site__hero .banner__title{padding-right:0}
  .site__hero .banner__tagline{left:26px;width:216px}
  .site__rooms{position:absolute;left:180px;top:213px;display:flex;gap:8px}
  .room{width:69px;height:82px}
  .room--label{
    border-top:1.5px solid var(--ink-plum);border-bottom:1.5px solid var(--ink-plum);
    display:flex;flex-direction:column;align-items:center;justify-content:center;
    font:400 9px/1 "Josefin Sans",sans-serif;color:var(--ink-plum);letter-spacing:2.5px;
  }
  .room--label em{font-style:normal;font-size:4px;color:var(--tan);margin:4px 0}
  .room--label b{font-weight:400;font-size:10px;letter-spacing:1.5px}
  .room--bed{background:linear-gradient(180deg,#e8e6e2 0%,#d7cfc6 60%,#6d5640 100%)}
  .room--sofa{background:linear-gradient(180deg,#e9e7e3 0%,#5b6068 55%,#8a6a3c 100%)}
  .room--dining{background:linear-gradient(180deg,#e6e9ea 0%,#cfc6b6 60%,#a9a39a 100%)}
</style>
</head>
<body>
<main class="canvas">

  <section class="banner banner--plum banner--top banner--shadow">
    <div class="banner__panel" role="img" aria-label="Softly faded mirrored dresser and vase behind a deep plum overlay">
      <svg class="banner__decor" viewBox="0 0 561 327" preserveAspectRatio="none" aria-hidden="true">
        <g class="banner__hearts" fill="currentColor">
          <path d="M470 150c0-30 40-45 58-15c18-30 58-15 58 15c0 35-58 70-58 90c0-20-58-55-58-90z"/>
          <path d="M20 60c0-14 19-21 27-7c8-14 27-7 27 7c0 16-27 33-27 42c0-9-27-26-27-42z"/>
          <path d="M500 40c0-9 12-13 17-4c5-9 17-5 17 4c0 10-17 20-17 26c0-6-17-16-17-26z"/>
        </g>
        <path class="banner__curve" d="M0 300C150 250 380 330 561 250" fill="none" stroke="currentColor" stroke-width="1.2"/>
      </svg>
      <p class="banner__kicker">FIND A LOOK YOU</p>
      <h1 class="banner__title">LOVE</h1>
      <p class="banner__tagline">Wide Range Of Quality Furniture For The<br>Bedroom, Dining Room or Living Room</p>
    </div>
    <div class="banner__photo" role="img" aria-label="Bedroom with upholstered wingback bed, mauve bedding, mirrored bedside table and lamp"></div>
  </section>

  <section class="banner banner--tan banner--bottom banner--shadow">
    <div class="banner__panel" role="img" aria-label="Softly faded mirrored dresser and vase behind a warm gold overlay">
      <svg class="banner__decor" viewBox="0 0 561 327" preserveAspectRatio="none" aria-hidden="true">
        <g class="banner__hearts" fill="currentColor">
          <path d="M470 150c0-30 40-45 58-15c18-30 58-15 58 15c0 35-58 70-58 90c0-20-58-55-58-90z"/>
          <path d="M20 60c0-14 19-21 27-7c8-14 27-7 27 7c0 16-27 33-27 42c0-9-27-26-27-42z"/>
          <path d="M500 40c0-9 12-13 17-4c5-9 17-5 17 4c0 10-17 20-17 26c0-6-17-16-17-26z"/>
        </g>
        <path class="banner__curve" d="M0 300C150 250 380 330 561 250" fill="none" stroke="currentColor" stroke-width="1.2"/>
      </svg>
      <p class="banner__kicker">FIND A LOOK YOU</p>
      <h2 class="banner__title">LOVE</h2>
      <p class="banner__tagline">Wide Range Of Quality Furniture For The<br>Bedroom, Dining Room or Living Room</p>
    </div>
    <div class="banner__photo" role="img" aria-label="Bedroom with upholstered wingback bed, mauve bedding, mirrored bedside table and lamp"></div>
  </section>

  <section class="site">
    <div class="site__notice">Free delivery on all orders this week only</div>
    <header class="site__header">
      <div class="site__brand">HARLOWE<small>FURNITURE</small></div>
      <div class="site__phone"><i></i>0300 555 0172</div>
      <div class="site__links"><span>Store Finder</span><span>My Account</span><span>Basket</span></div>
    </header>
    <nav class="site__nav"><span>HOME</span><span>BEDROOM ▾</span><span>LIVING ROOM ▾</span><span>DINING ROOM ▾</span><span>CONTACT ▾</span></nav>
    <div class="banner banner--plum site__hero" style="--s:0.45">
      <div class="banner__panel" role="img" aria-label="Softly faded mirrored dresser behind a deep plum overlay">
        <svg class="banner__decor" viewBox="0 0 561 327" preserveAspectRatio="none" aria-hidden="true">
          <g class="banner__hearts" fill="currentColor">
            <path d="M470 150c0-30 40-45 58-15c18-30 58-15 58 15c0 35-58 70-58 90c0-20-58-55-58-90z"/>
          </g>
          <path class="banner__curve" d="M0 300C150 250 380 330 561 250" fill="none" stroke="currentColor" stroke-width="1.2"/>
        </svg>
        <p class="banner__kicker">FIND A LOOK YOU</p>
        <p class="banner__title">LOVE</p>
        <p class="banner__tagline">Wide Range Of Quality Furniture For The<br>Bedroom, Dining Room or Living Room</p>
      </div>
      <div class="banner__photo" role="img" aria-label="Bedroom with upholstered bed and mirrored furniture"></div>
    </div>
    <div class="site__rooms">
      <div class="room room--label">SHOP<em>• BY •</em><b>ROOM</b></div>
      <div class="room room--bed" role="img" aria-label="Cream upholstered bed in a bright bedroom"></div>
      <div class="room room--sofa" role="img" aria-label="Grey buttoned sofa in a living room"></div>
      <div class="room room--dining" role="img" aria-label="Light dining table with upholstered chairs"></div>
    </div>
  </section>

</main>
</body>
</html>
```